Velsori Biotechnology needs a professional powerpoint design

We would like to re-design our powerpoint template(as attachment 1), it should be based on our current logo (as attachment 2). We hope the new powerpoint template could be more professional and like a biotechnology company with advanced technology.
Velsori Biotechnology is a contract development and manufacturing organization to provide high quality services to our clients in development, lead-in advanced technology and cGMP manufacturing of biopharmaceuticals from clinical to commercial manufacturing. We offers the advanced technology and services to become the best partner for clients from clinical to commercial manufacturing.
Reason: We would like to extend the deadline for this project so that designers can have more time to prepare, thanks.
Target Market(s)
Velsori Biotechnology is a contract development and manufacturing organization to provide high quality services to our clients in development, lead-in advanced technology and cGMP manufacturing of biopharmaceuticals from clinical to commercial manufacturing.
Velsori primary focus on development and manufacturing of glycoprotein pharmaceuticals against breast cancer, supplies KEP Taiwan with KEP-437 & KEP-438 for global clinical trials and commercialization in the future. Velsori offers the advanced technology and services to become the best partner for clients from clinical to commercial manufacturing.
Industry/Entity Type
Biotechnology
Requirements
Must have
- The new powerpoint design should based on our current logo.
Should not have
- The similar design with current powerpoint style. Please don't refer the design style of our current website http://www.velsori-example.com.tw/ as well, we will re-design it soon.

```html
<!DOCTYPE html>
<html lang="en">
<head>
<meta charset="utf-8">
<title>Velsori Biotechnology – Presentation Template</title>
<link href="https://fonts.googleapis.com/css2?family=Cabin:wght@400;600;700&display=swap" rel="stylesheet">
<style>
  :root {
    --canvas: #ffffff;
    --brand-blue: #2f5fb0;
    --brand-deep: #1f3f94;
    --brand-navy: #1a2d6b;
    --sky: #c5d7ef;
    --ice: #e7eef8;
    --ink: #3a3a3a;
    --muted: #666b73;
    --bar-green: #8cb63c;
    --bar-red: #e02b2b;
    --bar-blue: #2a52a8;
  }
  html, body {
    margin: 0;
    width: 1200px;
    height: 1200px;
    overflow: hidden;
    background: var(--canvas);
  }
  .sheet {
    position: relative;
    width: 1200px;
    height: 1200px;
  }
  .slide {
    position: absolute;
    width: 378px;
    height: 213px;
    background: #fff;
    box-shadow: 1px 2px 4px rgba(0,0,0,0.35);
    overflow: hidden;
  }
  .slide svg { display: block; width: 378px; height: 213px; }
  .slide text { font-family: 'Cabin', sans-serif; }
  .col-1 { left: 11px; } .col-2 { left: 413px; } .col-3 { left: 814px; }
  .row-1 { top: 30px; } .row-2 { top: 282px; } .row-3 { top: 535px; }

  .title { fill: var(--brand-deep); font-size: 17px; font-weight: 600; }
  .subtitle { fill: var(--muted); font-size: 8px; }
  .body { fill: var(--ink); font-size: 7.6px; }
  .body-sm { fill: var(--ink); font-size: 6.3px; }
  .brand-name { fill: var(--brand-navy); font-weight: 700; letter-spacing: 0.5px; }
  .brand-dot { fill: var(--brand-blue); }
  .cover-title { fill: #fff; font-size: 16px; font-weight: 600; }
  .cover-sub { fill: #fff; font-size: 7px; }
  .section-head { fill: var(--brand-deep); font-size: 10.5px; font-weight: 700; letter-spacing: 0.3px; }
  .bullet { fill: var(--brand-deep); }
  .donut-label { fill: var(--brand-deep); font-size: 7.5px; font-weight: 600; }
  .donut-value { fill: var(--brand-deep); font-size: 15px; }
  .axis-label { fill: var(--ink); font-size: 4.5px; }
  .chev-title { fill: #fff; font-size: 10px; font-weight: 700; letter-spacing: 1px; }
  .chev-body { fill: #fff; font-size: 6.6px; }
  .defs-holder { position: absolute; width: 0; height: 0; }
</style>
</head>
<body>
<svg class="defs-holder" aria-hidden="true">
  <defs>
    <linearGradient id="lab-blue" x1="0" y1="0" x2="1" y2="1">
      <stop offset="0" stop-color="#dfe9f6"/>
      <stop offset="0.5" stop-color="#8fb0da"/>
      <stop offset="1" stop-color="#c9d9ee"/>
    </linearGradient>
    <linearGradient id="lab-dark" x1="0" y1="0" x2="1" y2="1">
      <stop offset="0" stop-color="#1c3e78"/>
      <stop offset="0.6" stop-color="#4b78b4"/>
      <stop offset="1" stop-color="#23406f"/>
    </linearGradient>
    <linearGradient id="lab-scientist" x1="0" y1="0" x2="1" y2="1">
      <stop offset="0" stop-color="#e6eef6"/>
      <stop offset="0.6" stop-color="#b9cfe3"/>
      <stop offset="1" stop-color="#f2f5f8"/>
    </linearGradient>
    <linearGradient id="lab-wash" x1="0" y1="0" x2="1" y2="1">
      <stop offset="0" stop-color="#eef2f9"/>
      <stop offset="0.6" stop-color="#dbe4f2"/>
      <stop offset="1" stop-color="#e9eef7"/>
    </linearGradient>
    <linearGradient id="lab-glow" x1="0" y1="0" x2="1" y2="1">
      <stop offset="0" stop-color="#3a3f52"/>
      <stop offset="0.5" stop-color="#b7a07a"/>
      <stop offset="1" stop-color="#5a6a88"/>
    </linearGradient>
  </defs>
</svg>

<main class="sheet">

  <!-- Cover: pipette -->
  <section class="slide col-1 row-1">
    <svg viewBox="0 0 473 266">
      <path role="img" aria-label="Photo of a pipette dropping blue liquid into a test tube" d="M0,0 L473,0 L473,266 L375,266 Q300,110 0,40 Z" fill="url(#lab-blue)"/>
      <circle class="brand-dot" cx="30" cy="180" r="5"/>
      <text class="brand-name" x="40" y="186" font-size="18">VELSORI</text>
      <rect x="0" y="193" width="473" height="60" fill="var(--brand-blue)" opacity="0.95"/>
      <text class="cover-title" x="42" y="223">Lorem ipsum dolor</text>
      <text class="cover-sub" x="42" y="236">Lorem ipsum dolor sit amet, consetetur sadipscing</text>
    </svg>
  </section>

  <!-- Cover: scientist -->
  <section class="slide col-2 row-1">
    <svg viewBox="0 0 473 266">
      <path role="img" aria-label="Photo of a scientist in goggles and gloves pipetting into a test tube" d="M0,0 L473,0 L473,266 L375,266 Q300,110 0,40 Z" fill="url(#lab-scientist)"/>
      <circle class="brand-dot" cx="30" cy="180" r="5"/>
      <text class="brand-name" x="40" y="186" font-size="18">VELSORI</text>
      <rect x="0" y="193" width="473" height="60" fill="var(--brand-blue)" opacity="0.95"/>
      <text class="cover-title" x="42" y="223">Lorem ipsum dolor</text>
      <text class="cover-sub" x="42" y="236">Lorem ipsum dolor sit amet, consetetur sadipscing</text>
    </svg>
  </section>

  <!-- Cover: DNA -->
  <section class="slide col-3 row-1">
    <svg viewBox="0 0 473 266">
      <path role="img" aria-label="Photo of a gloved hand with a glowing DNA helix" d="M0,0 L473,0 L473,266 L375,266 Q300,110 0,40 Z" fill="url(#lab-dark)"/>
      <circle class="brand-dot" cx="30" cy="180" r="5"/>
      <text class="brand-name" x="40" y="186" font-size="18">VELSORI</text>
      <rect x="0" y="193" width="473" height="60" fill="var(--brand-blue)" opacity="0.95"/>
      <text class="cover-title" x="42" y="223">Lorem ipsum dolor</text>
      <text class="cover-sub" x="42" y="236">Lorem ipsum dolor sit amet, consetetur sadipscing</text>
    </svg>
  </section>

  <!-- Content: image + bullets -->
  <section class="slide col-1 row-2">
    <svg viewBox="0 0 473 266">
      <path role="img" aria-label="Photo of a pipette with blue liquid above test tubes" d="M0,0 L165,0 Q300,120 255,266 L0,266 Z" fill="url(#lab-blue)"/>
      <text class="section-head" x="278" y="54">LOREM IPSUM DOLOR</text>
      <circle class="bullet" cx="281" cy="74" r="1.6"/>
      <text class="body" x="290" y="77">
        <tspan x="290">Lorem ipsum dolor sit amet,</tspan>
        <tspan x="290" dy="11.5">consetetur sadipscing elitr, sed</tspan>
        <tspan x="290" dy="11.5">diam nonumy eirmod tempor</tspan>
        <tspan x="290" dy="11.5">invidunt ut</tspan>
      </text>
      <circle class="bullet" cx="281" cy="133" r="1.6"/>
      <text class="body" x="290" y="136">
        <tspan x="290">Labore et dolore magna</tspan>
        <tspan x="290" dy="11.5">aliquyam erat, sed diam</tspan>
        <tspan x="290" dy="11.5">voluptua.</tspan>
      </text>
      <circle class="bullet" cx="281" cy="180" r="1.6"/>
      <text class="body" x="290" y="183">
        <tspan x="290">At vero eos et accusam et justo</tspan>
        <tspan x="290" dy="11.5">duo dolores et ea rebum.</tspan>
      </text>
      <circle class="brand-dot" cx="404" cy="244" r="3"/>
      <text class="brand-name" x="410" y="248" font-size="11">VELSORI</text>
    </svg>
  </section>

  <!-- Content: bar chart -->
  <section class="slide col-2 row-2">
    <svg viewBox="0 0 473 266">
      <path d="M0,0 L57,0 Q25,80 0,160 Z" fill="var(--sky)"/>
      <path d="M57,0 Q25,80 0,160" fill="none" stroke="var(--brand-deep)" stroke-width="3"/>
      <path d="M446,0 Q400,130 385,266 L473,266 L473,0 Z" fill="var(--sky)"/>
      <path d="M446,0 Q400,130 385,266" fill="none" stroke="var(--brand-deep)" stroke-width="3"/>
      <text class="title" x="60" y="43">Lorem ipsum dolor sit amet</text>
      <text class="subtitle" x="60" y="58">Consetetur sadipscing elitr</text>
      <circle class="bullet" cx="53" cy="101" r="1.3"/>
      <text class="body-sm" x="62" y="103">
        <tspan x="62">Lorem ipsum dolor sit amet,</tspan>
        <tspan x="62" dy="10.5">consetetur sadipscing elitr, sed</tspan>
        <tspan x="62" dy="10.5">diam nonumy eirmod tempor</tspan>
        <tspan x="62" dy="10.5">invidunt ut</tspan>
      </text>
      <circle class="bullet" cx="53" cy="156" r="1.3"/>
      <text class="body-sm" x="62" y="158">
        <tspan x="62">Labore et dolore magna</tspan>
        <tspan x="62" dy="10.5">aliquyam erat, sed diam</tspan>
        <tspan x="62" dy="10.5">voluptua.</tspan>
      </text>
      <circle class="bullet" cx="53" cy="199" r="1.3"/>
      <text class="body-sm" x="62" y="201">
        <tspan x="62">At vero eos et accusam et justo</tspan>
        <tspan x="62" dy="10.5">duo dolores et ea rebum.</tspan>
      </text>
      <g class="bar-chart">
        <rect x="236" y="86" width="5" height="134" fill="var(--bar-green)"/>
        <rect x="243" y="145" width="5" height="75" fill="var(--bar-red)"/>
        <rect x="250" y="158" width="5" height="62" fill="var(--bar-blue)"/>
        <rect x="281" y="142" width="5" height="78" fill="var(--bar-green)"/>
        <rect x="289" y="82" width="5" height="138" fill="var(--bar-red)"/>
        <rect x="297" y="158" width="5" height="62" fill="var(--bar-blue)"/>
        <rect x="328" y="110" width="5" height="110" fill="var(--bar-green)"/>
        <rect x="336" y="164" width="5" height="56" fill="var(--bar-red)"/>
        <rect x="344" y="127" width="5" height="93" fill="var(--bar-blue)"/>
        <line x1="230" y1="220" x2="355" y2="220" stroke="#d0d0d0" stroke-width="0.6"/>
        <text class="axis-label" x="241" y="228">Text</text>
        <text class="axis-label" x="287" y="228">Text</text>
        <text class="axis-label" x="334" y="228">Text</text>
        <rect x="251" y="243" width="2" height="2" fill="var(--bar-green)"/>
        <text class="axis-label" x="254" y="246">Text</text>
        <rect x="284" y="243" width="2" height="2" fill="var(--bar-red)"/>
        <text class="axis-label" x="287" y="246">Text2</text>
        <rect x="318" y="243" width="2" height="2" fill="var(--bar-blue)"/>
        <text class="axis-label" x="321" y="246">Text3</text>
      </g>
      <circle class="brand-dot" cx="406" cy="240" r="3"/>
      <text class="brand-name" x="412" y="244" font-size="11">VELSORI</text>
    </svg>
  </section>

  <!-- Content: donut stats -->
  <section class="slide col-3 row-2">
    <svg viewBox="0 0 473 266">
      <path d="M0,0 L57,0 Q25,80 0,160 Z" fill="var(--sky)"/>
      <path d="M57,0 Q25,80 0,160" fill="none" stroke="var(--brand-deep)" stroke-width="3"/>
      <path d="M446,0 Q400,130 385,266 L473,266 L473,0 Z" fill="var(--sky)"/>
      <path d="M446,0 Q400,130 385,266" fill="none" stroke="var(--brand-deep)" stroke-width="3"/>
      <text class="title" x="60" y="43">Lorem ipsum dolor sit amet</text>
      <text class="donut-label" x="117" y="82" text-anchor="middle">LOREM IPSUM</text>
      <text class="donut-label" x="286" y="82" text-anchor="middle">LOREM IPSUM</text>
      <g transform="translate(117,151)">
        <circle r="50" fill="none" stroke="#e3e3e3" stroke-width="20" transform="scale(0.88)"/>
        <circle r="44" fill="none" stroke="var(--brand-deep)" stroke-width="17.6" stroke-dasharray="178 276" transform="rotate(-90)"/>
        <text class="donut-value" y="5" text-anchor="middle">+92%</text>
      </g>
      <g transform="translate(286,151)">
        <circle r="44" fill="none" stroke="#e3e3e3" stroke-width="17.6"/>
        <circle r="44" fill="none" stroke="var(--brand-deep)" stroke-width="17.6" stroke-dasharray="229 276" transform="rotate(-90)"/>
        <text class="donut-value" y="5" text-anchor="middle">+83%</text>
      </g>
      <text class="body-sm" x="200" y="228" text-anchor="middle">
        <tspan x="200">Lorem ipsum dolor sit amet, consetetur sadipscing elitr, sed diam nonumy eirmod</tspan>
        <tspan x="200" dy="9">tempor invidunt ut. Lorem ipsum dolor sit amet, consetetur sadipscing elitr, sed</tspan>
        <tspan x="200" dy="9">diam nonumy eirmod tempor invidunt ut.</tspan>
      </text>
      <circle class="brand-dot" cx="406" cy="240" r="3"/>
      <text class="brand-name" x="412" y="244" font-size="11">VELSORI</text>
    </svg>
  </section>

  <!-- Content: three image cards -->
  <section class="slide col-1 row-3">
    <svg viewBox="0 0 473 266">
      <rect role="img" aria-label="Faint background photo of a scientist in a laboratory" width="473" height="266" fill="url(#lab-wash)"/>
      <text class="title" x="26" y="30">Lorem ipsum dolor sit amet</text>
      <text class="subtitle" x="26" y="46">Consetetur sadipscing elitr</text>
      <circle class="brand-dot" cx="395" cy="27" r="3"/>
      <text class="brand-name" x="401" y="31" font-size="11">VELSORI</text>
      <rect role="img" aria-label="Photo of a gloved hand holding a glowing sphere" x="33" y="72" width="127" height="70" fill="url(#lab-glow)"/>
      <rect role="img" aria-label="Photo of a gloved hand with a DNA helix" x="172" y="72" width="127" height="70" fill="url(#lab-dark)"/>
      <rect role="img" aria-label="Photo of a pipette with blue liquid" x="312" y="72" width="127" height="70" fill="url(#lab-blue)"/>
      <text class="body-sm" y="156" text-anchor="middle">
        <tspan x="97">Lorem ipsum dolor sit amet,</tspan>
        <tspan x="97" dy="9.5">consetetur sadipscing elitr, sed</tspan>
        <tspan x="97" dy="9.5">diam nonumy eirmod tempor</tspan>
        <tspan x="97" dy="9.5">invidunt ut labore et dolore magna</tspan>
        <tspan x="97" dy="9.5">aliquyam erat, sed diam</tspan>
      </text>
      <text class="body-sm" y="156" text-anchor="middle">
        <tspan x="236">Lorem ipsum dolor sit amet,</tspan>
        <tspan x="236" dy="9.5">consetetur sadipscing elitr, sed</tspan>
        <tspan x="236" dy="9.5">diam nonumy eirmod tempor</tspan>
        <tspan x="236" dy="9.5">invidunt ut labore et dolore magna</tspan>
        <tspan x="236" dy="9.5">aliquyam erat, sed diam</tspan>
      </text>
      <text class="body-sm" y="156" text-anchor="middle">
        <tspan x="375">Lorem ipsum dolor sit amet,</tspan>
        <tspan x="375" dy="9.5">consetetur sadipscing elitr, sed</tspan>
        <tspan x="375" dy="9.5">diam nonumy eirmod tempor</tspan>
        <tspan x="375" dy="9.5">invidunt ut labore et dolore magna</tspan>
        <tspan x="375" dy="9.5">aliquyam erat, sed diam</tspan>
      </text>
    </svg>
  </section>

  <!-- Content: stacked images with text -->
  <section class="slide col-2 row-3">
    <svg viewBox="0 0 473 266">
      <rect role="img" aria-label="Faint background photo of a scientist in a laboratory" width="473" height="266" fill="url(#lab-wash)"/>
      <text class="title" x="26" y="30">Lorem ipsum dolor sit amet</text>
      <text class="subtitle" x="26" y="46">Consetetur sadipscing elitr</text>
      <circle class="brand-dot" cx="395" cy="27" r="3"/>
      <text class="brand-name" x="401" y="31" font-size="11">VELSORI</text>
      <rect role="img" aria-label="Photo of a gloved hand holding a glowing sphere" x="25" y="62" width="157" height="62" fill="url(#lab-glow)"/>
      <rect role="img" aria-label="Photo of a gloved hand with a DNA helix" x="25" y="126" width="157" height="62" fill="url(#lab-dark)"/>
      <rect role="img" aria-label="Photo of a scientist pipetting into a test tube" x="25" y="190" width="157" height="61" fill="url(#lab-scientist)"/>
      <text class="body-sm" x="190" y="81">
        <tspan x="190">Lorem ipsum dolor sit amet, consetetur sadipscing elitr, sed diam</tspan>
        <tspan x="190" dy="9.5">nonumy eirmod tempor invidunt ut labore et dolore magna aliquyam</tspan>
        <tspan x="190" dy="9.5">erat, sed diam voluptua. At vero eos et accusam et justo duo dolores</tspan>
        <tspan x="190" dy="9.5">et ea rebum.</tspan>
      </text>
      <text class="body-sm" x="190" y="145">
        <tspan x="190">Lorem ipsum dolor sit amet, consetetur sadipscing elitr, sed diam</tspan>
        <tspan x="190" dy="9.5">nonumy eirmod tempor invidunt ut labore et dolore magna aliquyam</tspan>
        <tspan x="190" dy="9.5">erat, sed diam voluptua. At vero eos et accusam et justo duo dolores</tspan>
        <tspan x="190" dy="9.5">et ea rebum.</tspan>
      </text>
      <text class="body-sm" x="190" y="208">
        <tspan x="190">Lorem ipsum dolor sit amet, consetetur sadipscing elitr, sed diam</tspan>
        <tspan x="190" dy="9.5">nonumy eirmod tempor invidunt ut labore et dolore magna aliquyam</tspan>
        <tspan x="190" dy="9.5">erat, sed diam voluptua. At vero eos et accusam et justo duo dolores</tspan>
        <tspan x="190" dy="9.5">et ea rebum.</tspan>
      </text>
    </svg>
  </section>

  <!-- Content: process chevrons -->
  <section class="slide col-3 row-3">
    <svg viewBox="0 0 473 266">
      <rect role="img" aria-label="Faint background photo of a scientist in a laboratory" width="473" height="266" fill="url(#lab-wash)"/>
      <text class="title" x="26" y="30">Lorem ipsum dolor sit amet</text>
      <text class="subtitle" x="26" y="46">Consetetur sadipscing elitr</text>
      <circle class="brand-dot" cx="395" cy="27" r="3"/>
      <text class="brand-name" x="401" y="31" font-size="11">VELSORI</text>
      <path d="M45,82 L165,82 L192,158 L165,235 L45,235 L72,158 Z" fill="var(--brand-deep)"/>
      <path d="M168,82 L287,82 L314,158 L287,235 L168,235 L195,158 Z" fill="#6b8fcb" opacity="0.85"/>
      <path d="M290,82 L408,82 L435,158 L408,235 L290,235 L317,158 Z" fill="#c4cfe0" opacity="0.8"/>
      <text class="chev-title" x="86" y="106">TITLE</text>
      <text class="chev-body" x="86" y="122">
        <tspan x="86">Lorem ipsum dolor s</tspan>
        <tspan x="86" dy="10.5">it amet, consetetur</tspan>
        <tspan x="86" dy="10.5">sadipscing elitr, sed</tspan>
        <tspan x="86" dy="10.5">diam nonumy eirmo</tspan>
        <tspan x="86" dy="10.5">d. Tempor invidunt</tspan>
        <tspan x="86" dy="10.5">ut labore et dolore</tspan>
        <tspan x="86" dy="10.5">magna aliquyam era</tspan>
        <tspan x="86" dy="10.5">t, sed diam voluptua</tspan>
      </text>
      <text class="chev-title" x="209" y="106">TITLE</text>
      <text class="chev-body" x="209" y="122">
        <tspan x="209">Lorem ipsum dolor s</tspan>
        <tspan x="209" dy="10.5">it amet, consetetur</tspan>
        <tspan x="209" dy="10.5">sadipscing elitr, sed</tspan>
        <tspan x="209" dy="10.5">diam nonumy eirmo</tspan>
        <tspan x="209" dy="10.5">d. Tempor invidunt</tspan>
        <tspan x="209" dy="10.5">ut labore et dolore</tspan>
        <tspan x="209" dy="10.5">magna aliquyam era</tspan>
        <tspan x="209" dy="10.5">t, sed diam voluptua</tspan>
      </text>
      <text class="chev-title" x="331" y="106" style="fill:var(--ink)">TITLE</text>
      <text class="chev-body" x="331" y="122" style="fill:var(--ink)">
        <tspan x="331">Lorem ipsum dolor s</tspan>
        <tspan x="331" dy="10.5">it amet, consetetur</tspan>
        <tspan x="331" dy="10.5">sadipscing elitr, sed</tspan>
        <tspan x="331" dy="10.5">diam nonumy eirmo</tspan>
        <tspan x="331" dy="10.5">d. Tempor invidunt</tspan>
        <tspan x="331" dy="10.5">ut labore et dolore</tspan>
        <tspan x="331" dy="10.5">magna aliquyam era</tspan>
        <tspan x="331" dy="10.5">t, sed diam voluptua</tspan>
      </text>
    </svg>
  </section>

</main>
</body>
</html>
```